Natural & Organic Skin Care Line labels

TALURNE is start up company for all natural and organic beauty products needing labels. KISS method/less is more so no graphics. would like "natural background color" black faunts, pop of color matching scent. Will attach example I made on Mac Word.
Updates

I would like to thank the designers for very nice work.  Believing I jumped the gun with a project I was not fully prepared for, I am placing it on hold.

Target Market(s)

Mostly women with middle to upper income

Industry/Entity Type

It Company

Requirements
Must have
• Cosmetic labeling requires labels list INCI (attached example), and Net Wt.

```html
<!DOCTYPE html>
<html lang="en">
<head>
<meta charset="UTF-8">
<title>TALURNE Organic — Whipped Lip Butter Labels</title>
<link rel="stylesheet" href="https://fonts.googleapis.com/css2?family=Quicksand:wght@400;500&family=Poiret+One&family=Playball&family=Arimo:wght@400;700&family=Tinos&display=swap">
<style>
  :root {
    --sheet: #e2d4a4;
    --sheet-edge: #b9ab80;
    --label-brown: #6a5a47;
    --label-brown-light: #8a7654;
    --ink-light: #ffffff;
    --band-orange-lemongrass: #e8761d;
    --band-vanilla-sandalwood: #d8c39a;
    --band-lemon: #ece66c;
    --band-orange-vanilla: #e2a56b;
    --band-peppermint: #c6d64b;
  }
  * { box-sizing: border-box; margin: 0; padding: 0; }
  html, body { width: 1200px; height: 834px; overflow: hidden; background: var(--sheet); }
  .label-sheet {
    position: relative;
    width: 1200px; height: 834px;
    background: var(--sheet);
    border: 2px solid var(--sheet-edge);
  }
  .lip-label {
    position: absolute;
    width: 350px; height: 350px;
    color: var(--ink-light);
    text-align: center;
  }
  .lip-label svg.label-face {
    position: absolute; inset: 0;
    width: 350px; height: 350px;
    filter: drop-shadow(0 0 14px rgba(60, 45, 25, 0.55));
    overflow: visible;
  }
  .brand-name, .brand-line {
    position: absolute; left: 0; right: 0;
    font-family: "Quicksand", sans-serif;
    font-weight: 400;
    font-size: 33px;
    line-height: 1;
  }
  .brand-name { top: 28px; letter-spacing: 0.5px; }
  .brand-line { top: 64px; }
  .product-type {
    position: absolute; left: 0; right: 0; top: 124px;
    font-family: "Poiret One", sans-serif;
    font-size: 27px;
    line-height: 1;
    font-weight: 400;
    text-shadow: 0 0 0.6px #fff;
  }
  .scent-name {
    position: absolute; left: 0; right: 0; top: 175px;
    font-family: "Playball", cursive;
    font-size: 25px;
    line-height: 1;
  }
  .scent-name.is-large { font-size: 30px; top: 171px; }
  .inci-list {
    position: absolute; left: 45px; right: 45px; top: 210px;
    font-family: "Arimo", sans-serif;
    font-size: 8.6px;
    line-height: 1.22;
  }
  .inci-list b { font-weight: 700; }
  .net-weight {
    position: absolute; left: 0; right: 0; top: 290px;
    font-family: "Tinos", serif;
    font-size: 13px;
  }
  .label-orange-lemongrass { left: 44px; top: 96px; }
  .label-vanilla-sandalwood { left: 419px; top: 96px; }
  .label-lemon { left: 794px; top: 96px; }
  .label-orange-vanilla { left: 230px; top: 431px; }
  .label-peppermint { left: 606px; top: 431px; }
  .label-orange-lemongrass .scent-band { fill: var(--band-orange-lemongrass); }
  .label-vanilla-sandalwood .scent-band { fill: var(--band-vanilla-sandalwood); }
  .label-lemon .scent-band { fill: var(--band-lemon); }
  .label-orange-vanilla .scent-band { fill: var(--band-orange-vanilla); }
  .label-peppermint .scent-band { fill: var(--band-peppermint); }
</style>
</head>
<body>
<main class="label-sheet">

  <section class="lip-label label-orange-lemongrass">
    <svg class="label-face" viewBox="0 0 350 350" aria-hidden="true">
      <defs>
        <radialGradient id="stone" cx="50%" cy="50%" r="50%">
          <stop offset="0%" stop-color="#7a6850"/>
          <stop offset="100%" stop-color="#665643"/>
        </radialGradient>
      </defs>
      <circle cx="175" cy="175" r="175" fill="url(#stone)" role="img" aria-label="Speckled brown stone texture background"/>
      <polygon class="scent-band" points="20,111 333,109 331,168 21,170"/>
    </svg>
    <div class="brand-name">TALURNE</div>
    <div class="brand-line">Organic</div>
    <div class="product-type">Whipped Lip Butter</div>
    <div class="scent-name">Orange Lemongrass</div>
    <p class="inci-list"><b>INCI:</b> CymbopogonSchoenathus (Lemongrass) Oil, Citrus AurantiumDulcis (Organic Orange) Peel Oil, ButyrospermumParkii (Organic Shea) Butter, Beeswax, CocosNucifera (Organic Coconut) Oil, Rosa Mosqueta (Organic Rose Hip) Oil, RosmarinusOfficinalis (Rosemary) Leaf Extract, Tocopherol (Vitamin E)</p>
    <div class="net-weight">Net Wt. .30oz(8.5g)</div>
  </section>

  <section class="lip-label label-vanilla-sandalwood">
    <svg class="label-face" viewBox="0 0 350 350" aria-hidden="true">
      <circle cx="175" cy="175" r="175" fill="url(#stone)" role="img" aria-label="Speckled brown stone texture background"/>
      <polygon class="scent-band" points="20,111 333,109 331,168 21,170"/>
    </svg>
    <div class="brand-name">TALURNE</div>
    <div class="brand-line">Organic</div>
    <div class="product-type">Whipped Lip Butter</div>
    <div class="scent-name">Vanilla &amp; Sandlewood</div>
    <p class="inci-list"><b>INCI:</b>Santalum Album (Organic Sandlewood) Oil, Vanilla PlanifoliaExtract, Flavor (Aroma), ButyrospermumParkii (Organic Shea) Butter, Beeswax, CocosNucifera (Organic Coconut) Oil, Rosa Mosqueta (Organic Rose Hip) Oil, RosmarinusOfficinalis (Rosemary) Leaf Extract, Tocopherol (Vitamin E)</p>
    <div class="net-weight">Net Wt. .30oz(8.5g)</div>
  </section>

  <section class="lip-label label-lemon">
    <svg class="label-face" viewBox="0 0 350 350" aria-hidden="true">
      <circle cx="175" cy="175" r="175" fill="url(#stone)" role="img" aria-label="Speckled brown stone texture background"/>
      <polygon class="scent-band" points="20,111 333,109 331,168 21,170"/>
    </svg>
    <div class="brand-name">TALURNE</div>
    <div class="brand-line">Organic</div>
    <div class="product-type">Whipped Lip Butter</div>
    <div class="scent-name is-large">Lemon</div>
    <p class="inci-list"><b>INCI:</b> Citrus Limonium (Lemon) Oil, ButyrospermumParkii (Organic Shea) Butter, Beeswax, CocosNucifera (Organic Coconut) Oil, Rosa Mosqueta (Organic Rose Hip) Oil, RosmarinusOfficinalis (Rosemary) Leaf Extract, Tocopherol (Vitamin E)</p>
    <div class="net-weight">Net Wt. .30oz(8.5g)</div>
  </section>

  <section class="lip-label label-orange-vanilla">
    <svg class="label-face" viewBox="0 0 350 350" aria-hidden="true">
      <circle cx="175" cy="175" r="175" fill="url(#stone)" role="img" aria-label="Speckled brown stone texture background"/>
      <polygon class="scent-band" points="20,111 333,109 331,168 21,170"/>
    </svg>
    <div class="brand-name">TALURNE</div>
    <div class="brand-line">Organic</div>
    <div class="product-type">Whipped Lip Butter</div>
    <div class="scent-name">Orange Vanilla</div>
    <p class="inci-list"><b>INCI:</b> Citrus Sinensis (Orange) Oil, Flavor (Aroma) Vanilla Planifolia Extract, ButyrospermumParkii (Organic Shea) Butter, Beeswax, CocosNucifera (Organic Coconut) Oil, Rosa Mosqueta (Organic Rose Hip) Oil, RosmarinusOfficinalis (Rosemary) Leaf Extract, Tocopherol (Vitamin E)</p>
    <div class="net-weight">Net Wt. .30oz(8.5g)</div>
  </section>

  <section class="lip-label label-peppermint">
    <svg class="label-face" viewBox="0 0 350 350" aria-hidden="true">
      <circle cx="175" cy="175" r="175" fill="url(#stone)" role="img" aria-label="Speckled brown stone texture background"/>
      <polygon class="scent-band" points="20,111 333,109 331,168 21,170"/>
    </svg>
    <div class="brand-name">TALURNE</div>
    <div class="brand-line">Organic</div>
    <div class="product-type">Whipped Lip Butter</div>
    <div class="scent-name">Peppermint</div>
    <p class="inci-list"><b>INCI:</b> MenthaPiperita (Peppermint) Oil, ButyrospermumParkii (Organic Shea) Butter, Beeswax, CocosNucifera (Organic Coconut) Oil, Rosa Mosqueta (Organic Rose Hip) Oil, RosmarinusOfficinalis (Rosemary) Leaf Extract, Tocopherol (Vitamin E)</p>
    <div class="net-weight">Net Wt. .30oz(8.5g)</div>
  </section>

</main>
</body>
</html>
```